Brackenridge Strength Studio Chronic Pain Flyer

Double sided DL flyer required to promote a strength training studio to sufferers of chronic pain. Flyer will be displayed in osteopathy, chiropractic and massage clinics. Flyer should be clean, professional and appeal to an older (40+) demographic.

Target Market(s)

Chronic pain sufferers. Age 40+

Industry/Entity Type

Health And Wellness

Colors

Designer to choose colors to be used in the design.

Requirements
Must have
• See attached files for text copy and logo. Image(s) of people strength training with a coach or personal trainer, as well as images depicting pain in common parts of the body (such as those pictured in the supplied mock up)
• website address: brackenridgestrengthstudio.example.com.au
• phone number : 0452 918 304
• Street address: 4/63 Juniper Hollow Rd, Brackenridge
Nice to have
• Images such as in the attached files.

```html
<!DOCTYPE html>
<html lang="en">
<head>
<meta charset="utf-8">
<title>Brackenridge Strength Studio – Health Through Strength</title>
<link rel="stylesheet" href="https://fonts.googleapis.com/css2?family=Roboto+Condensed:wght@400;700&display=swap">
<style>
  :root {
    --ink: #111111;
    --red: #d4252b;
    --white: #ffffff;
    --paper: #f4f4f4;
    --band-grey: rgba(200, 200, 200, 0.55);
    --black: #050505;
    --photo-light: #e6e6e6;
    --photo-mid: #bdbdbd;
    --photo-dark: #8a8a8a;
  }
  * { margin: 0; padding: 0; box-sizing: border-box; }
  html, body { width: 1200px; height: 572px; overflow: hidden; background: var(--white); }
  .flyer {
    position: relative;
    width: 1200px;
    height: 572px;
    overflow: hidden;
    background: var(--paper);
    font-family: "Roboto Condensed", "Arial Narrow", sans-serif;
    color: var(--ink);
  }
  .photo-knee {
    position: absolute;
    left: 110px; top: 0;
    width: 470px; height: 430px;
    background: radial-gradient(ellipse at 55% 55%, var(--photo-mid) 0%, var(--photo-light) 55%, rgba(244,244,244,0) 80%);
    opacity: 0.8;
  }
  .photo-shoulder {
    position: absolute;
    left: 680px; top: 0;
    width: 520px; height: 430px;
    background:
      radial-gradient(circle at 225px 145px, rgba(230, 60, 60, 0.75) 0%, rgba(230, 60, 60, 0.3) 45px, rgba(230,60,60,0) 90px),
      radial-gradient(ellipse at 60% 55%, var(--photo-dark) 0%, var(--photo-mid) 45%, var(--photo-light) 75%, rgba(244,244,244,0) 95%);
  }
  .headline-band {
    position: absolute;
    left: 0; top: 29px;
    width: 745px; height: 240px;
    background: var(--band-grey);
  }
  .headline {
    position: absolute;
    left: 114px; top: 42px;
    font-weight: 700;
    font-size: 70px;
    line-height: 74px;
    letter-spacing: -0.5px;
  }
  .headline .accent { color: var(--red); display: block; }
  .tagline {
    position: absolute;
    left: 120px; top: 218px;
    font-weight: 700;
    font-size: 33px;
    text-transform: uppercase;
    letter-spacing: 0.3px;
  }
  .tagline .accent { color: var(--red); }
  .body-copy {
    position: absolute;
    left: 120px; top: 288px;
    width: 520px;
    font-size: 16px;
    line-height: 20px;
  }
  .body-copy p + p { margin-top: 10px; }
  .footer-band {
    position: absolute;
    left: 0; top: 423px;
    width: 1200px; height: 149px;
    background: var(--black);
  }
  .cta-strip {
    position: absolute;
    left: 0; top: 423px;
    width: 900px; height: 40px;
    background: linear-gradient(90deg, #3a3a3a 0%, #8c8c8c 55%, #d6d6d6 80%, rgba(214,214,214,0.2) 100%);
  }
  .cta {
    position: absolute;
    left: 120px; top: 430px;
    font-weight: 700;
    font-size: 20px;
    color: var(--white);
  }
  .contact-phone, .contact-address {
    position: absolute;
    top: 485px;
    font-size: 18px;
    color: var(--white);
  }
  .contact-phone { left: 114px; }
  .contact-address { left: 364px; display: flex; align-items: center; gap: 10px; }
  .website {
    position: absolute;
    left: 114px; top: 513px;
    font-weight: 700;
    font-size: 30px;
    color: var(--red);
  }
  .brand-oval { position: absolute; left: 840px; top: 360px; }
  .brand-name {
    position: absolute;
    left: 900px; top: 455px;
    width: 290px;
    text-align: center;
    font-weight: 700;
    font-size: 22px;
    line-height: 26px;
    text-transform: uppercase;
    color: var(--white);
  }
</style>
</head>
<body>
<main class="flyer">
  <div class="photo-knee" role="img" aria-label="Black and white photo of hands holding a painful knee"></div>
  <div class="photo-shoulder" role="img" aria-label="Black and white photo of a man holding his sore shoulder, with red glow marking the pain"></div>

  <div class="headline-band"></div>
  <h1 class="headline">Health Through<span class="accent">Strength</span></h1>
  <h2 class="tagline">You <span class="accent">don’t</span> have to live in pain.</h2>

  <div class="body-copy">
    <p>Strength training has been shown to improve many chronic pain conditions and is now being routinely recommended by medical health professionals.</p>
    <p>Our private studio provides high quality strength training by expert strength coaches. We’ve helped countless people improve or eliminate chronic pain.</p>
  </div>

  <div class="footer-band"></div>
  <div class="cta-strip"></div>
  <p class="cta">Contact us today and find out how we can help you.</p>

  <p class="contact-phone">Contact: 0452 918 304</p>
  <p class="contact-address">
    <svg width="16" height="22" viewBox="0 0 16 22" aria-hidden="true">
      <path d="M8 0C3.6 0 0 3.5 0 7.9 0 13.5 8 22 8 22s8-8.5 8-14.1C16 3.5 12.4 0 8 0z" fill="#ffffff"/>
      <circle cx="8" cy="8" r="3.2" fill="#050505"/>
    </svg>
    4/63 Juniper Hollow Rd, Brackenridge
  </p>
  <p class="website">brackenridgestrengthstudio.example.com.au</p>

  <svg class="brand-oval" width="360" height="212" viewBox="0 0 360 212" aria-hidden="true">
    <ellipse cx="230" cy="140" rx="215" ry="130" fill="#050505"/>
  </svg>
  <p class="brand-name">Brackenridge<br>Strength Studio</p>
</main>
</body>
</html>
```